Brookfarrow Osteopathy and dry needling business card

Business card for Brookfarrow Osteopathy and Dry Needling.

Industry/Entity Type

Health

Contact Information for Business Card

I do not have a phone number yet. I also do not have an email address yet. The physical address is: 48 Lower Crane Street Brookfarrow The website is: www.brookfarrowosteosteopathy.example My details are: Dr Martin Pellowe, Osteopath (B.Clin.Sci (Ost) M.Ost BSC ECON (Hons)

Colors
0094D4
00A9DD
6FCCEA
C7EBF8
E9F6FB

Requirements
Must have
• logo on the back
Nice to have
• Maybe a space for me to write an appointment time and date on the card.

```html
<!DOCTYPE html>
<html lang="en">
<head>
<meta charset="utf-8">
<title>Brookfarrow Osteopathy and Dry Needling – Business Card</title>
<link rel="stylesheet" href="https://fonts.googleapis.com/css2?family=Poppins:wght@400;500;600;700&display=swap">
<style>
  :root {
    --backdrop: #d6d6d6;
    --card: #ffffff;
    --brand-blue: #0094d4;
    --accent-orange: #f7941d;
    --ink-dark: #1d1d1d;
    --ink-grey: #4a4a4a;
    --rule-grey: #8a8a8a;
  }
  html, body {
    margin: 0;
    padding: 0;
    width: 946px;
    height: 1200px;
    overflow: hidden;
    background: var(--backdrop);
    font-family: "Poppins", sans-serif;
  }
  .canvas { position: relative; width: 946px; height: 1200px; }
  .card {
    position: absolute;
    left: 56px;
    width: 833px;
    height: 476px;
    background: var(--card);
    box-shadow: 0 4px 10px rgba(0,0,0,0.22);
    overflow: hidden;
  }
  .card--front { top: 98px; }
  .card--back { top: 626px; }
  .card svg.swoosh { position: absolute; left: 0; top: 0; width: 833px; height: 476px; }

  .brand-mark {
    position: absolute;
    display: flex;
    flex-direction: column;
    align-items: center;
    justify-content: center;
    text-align: center;
    color: var(--brand-blue);
    font-weight: 600;
    border: 2px solid var(--brand-blue);
    border-radius: 50%;
    box-sizing: border-box;
    line-height: 1.25;
  }
  .card--front .brand-mark { left: 329px; top: 74px; width: 174px; height: 174px; font-size: 15px; }
  .card--back .brand-mark { left: 79px; top: 134px; width: 218px; height: 218px; font-size: 19px; }

  .appointment-title {
    position: absolute;
    left: 0; right: 0; top: 250px;
    text-align: center;
    font-size: 28px;
    font-weight: 600;
    letter-spacing: 2.5px;
    color: var(--ink-grey);
    margin: 0;
  }
  .appointment-field {
    position: absolute;
    top: 310px;
    display: flex;
    align-items: flex-end;
    gap: 9px;
    color: var(--brand-blue);
    font-size: 28px;
    font-weight: 600;
  }
  .appointment-field .write-line {
    width: 221px;
    border-bottom: 1px solid var(--rule-grey);
    margin-bottom: 8px;
  }
  .appointment-field--date { left: 97px; }
  .appointment-field--time { left: 437px; }

  .practitioner {
    position: absolute;
    left: 433px;
    top: 122px;
    width: 370px;
  }
  .practitioner-name {
    margin: 0;
    font-size: 33px;
    font-weight: 700;
    line-height: 1;
    color: var(--card);
    letter-spacing: -0.5px;
  }
  .practitioner-name .title-first { color: var(--accent-orange); }
  .practitioner-role {
    margin: 6px 0 0;
    font-size: 23px;
    font-weight: 700;
    letter-spacing: 2.5px;
    color: var(--ink-dark);
    line-height: 1;
  }
  .practitioner-credentials {
    margin: 8px 0 0;
    font-size: 18px;
    font-weight: 500;
    color: var(--card);
    letter-spacing: -0.3px;
  }
  .divider {
    height: 1px;
    width: 357px;
    background: rgba(255,255,255,0.8);
    margin: 8px 0 14px;
  }
  .contact-list { list-style: none; margin: 0; padding: 0; }
  .contact-item {
    display: flex;
    align-items: center;
    gap: 13px;
    height: 35px;
    color: var(--card);
    font-size: 16.5px;
    font-weight: 500;
    white-space: nowrap;
  }
  .contact-icon {
    width: 28px; height: 28px;
    border-radius: 50%;
    background: var(--card);
    display: flex; align-items: center; justify-content: center;
    flex: none;
  }
</style>
</head>
<body>
<div class="canvas">

  <section class="card card--front" aria-label="Appointment card">
    <svg class="swoosh" viewBox="0 0 833 476" aria-hidden="true">
      <path d="M73 476 Q440 330 820 476 Z" fill="var(--brand-blue)"/>
      <path d="M240 420 Q520 382 770 476 L825 476 Q560 380 240 420 Z" fill="var(--brand-blue)"/>
    </svg>
    <div class="brand-mark">Brookfarrow<br>Osteopathy<br>&amp; Dry Needling</div>
    <h2 class="appointment-title">YOUR NEXT APPOINTMENT</h2>
    <div class="appointment-field appointment-field--date"><span>Date</span><span class="write-line"></span></div>
    <div class="appointment-field appointment-field--time"><span>Time</span><span class="write-line"></span></div>
  </section>

  <section class="card card--back" aria-label="Practitioner card">
    <svg class="swoosh" viewBox="0 0 833 476" aria-hidden="true">
      <path d="M252 0 Q470 238 249 476 L833 476 L833 0 Z" fill="var(--brand-blue)"/>
      <path d="M290 0 Q480 238 286 476" fill="none" stroke="var(--card)" stroke-width="7"/>
      <path d="M252 0 Q445 180 362 260 Q400 140 270 0 Z" fill="var(--card)"/>
    </svg>
    <div class="brand-mark">Brookfarrow<br>Osteopathy<br>&amp; Dry Needling</div>

    <div class="practitioner">
      <h1 class="practitioner-name"><span class="title-first">DR MARTIN</span> PELLOWE</h1>
      <p class="practitioner-role">OSTEOPATH</p>
      <p class="practitioner-credentials">(B.Clin.Sci (Ost) M.Ost BSC ECON (Hons)</p>
      <div class="divider"></div>
      <ul class="contact-list">
        <li class="contact-item">
          <span class="contact-icon">
            <svg width="16" height="16" viewBox="0 0 24 24" aria-hidden="true"><path fill="var(--accent-orange)" d="M6.6 10.8a15.1 15.1 0 0 0 6.6 6.6l2.2-2.2a1 1 0 0 1 1-.25 11.4 11.4 0 0 0 3.6.6 1 1 0 0 1 1 1V20a1 1 0 0 1-1 1A17 17 0 0 1 3 4a1 1 0 0 1 1-1h3.5a1 1 0 0 1 1 1c0 1.25.2 2.45.6 3.6a1 1 0 0 1-.25 1z"/></svg>
          </span>555 014 2387
        </li>
        <li class="contact-item">
          <span class="contact-icon">
            <svg width="16" height="16" viewBox="0 0 24 24" aria-hidden="true"><path fill="var(--accent-orange)" d="M12 2a7 7 0 0 0-7 7c0 5.2 7 13 7 13s7-7.8 7-13a7 7 0 0 0-7-7zm0 9.5A2.5 2.5 0 1 1 12 6.5a2.5 2.5 0 0 1 0 5z"/></svg>
          </span>48 Lower Crane Street Brookfarrow
        </li>
        <li class="contact-item">
          <span class="contact-icon">
            <svg width="16" height="16" viewBox="0 0 24 24" aria-hidden="true"><g fill="none" stroke="var(--accent-orange)" stroke-width="2"><circle cx="12" cy="12" r="9"/><ellipse cx="12" cy="12" rx="4" ry="9"/><path d="M3 12h18M5 7h14M5 17h14"/></g></svg>
          </span>www.brookfarrowosteosteopathy.example
        </li>
      </ul>
    </div>
  </section>

</div>
</body>
</html>
```